Web Design for Small Healthcare Startup

Hello,

We are seeking a Website Design for a healthcare company focusing on mobile vaccinations, employee health and wellness services onsite at businesses, and consulting services relating to Healthcare Entities in WA state. Our company’s mission is to “To aid in a healthier workplace”. Vitality Caravan will provide on-site wellness services to employers that simplify and streamline employee preventative health as well as onsite consulting services to help with compliance of Healthcare Entities.

We are seeking a Website Design for Vitality Caravan, PLLC. Our company’s mission is to provide mobile health and wellness services to employers onsite at their businesses. These services include mobile vaccinations clinics for employees as well as wellness and health screenings. The company will also offer healtcare compliance consulting services for Healthcare Entities. The company was founded to bring these important healthcare services to businesses and keep employees healthy. Healthy employees are the cornerstone to a great business and we want to help orginazations achieve their goals of having a healthy productive workforce.

We are looking for a moderin website design that will need to be coded. We have attached our current logo design for reference as well as a brief questionare regarding our business for your information (not necessary to include all information). We would like something SEO friendly and easy to navigate.

Thank you!

Vitality Caravan, PLLC

Target Market(s)

Small Businesses

Industry/Entity Type

Healthcare

Coding

Coded - Design and coding required

Number of Pages Required

1 page

Requirements
Nice to have
• SEO Friendly, Incorporate Logo

```html
<!DOCTYPE html>
<html lang="en">
<head>
<meta charset="utf-8">
<title>Vitality Caravan, PLLC – Mobile Workplace Vaccine Clinics</title>
<link href="https://fonts.googleapis.com/css2?family=Poppins:wght@300;400;500;600;700;800&display=swap" rel="stylesheet">
<style>
:root{
  --navy:#0b2150;
  --blue:#0a3aa8;
  --blue-dark:#062e8e;
  --ink:#0d2447;
  --text:#333a48;
  --magenta:#9b2a8f;
  --teal:#3aa9b8;
  --light:#e9eef8;
  --white:#fff;
}
*{box-sizing:border-box;margin:0;padding:0}
html,body{width:1200px;height:3262px;overflow:hidden}
body{font-family:"Poppins",sans-serif;color:var(--text);background:var(--white);position:relative}
.abs{position:absolute}
a{color:inherit;text-decoration:none}

/* top bar & header */
.topbar{position:absolute;right:0;top:0;width:516px;height:33px;background:var(--navy);clip-path:polygon(0 0,100% 0,100% 100%,36px 100%);color:#fff;font-size:13px;display:flex;align-items:center;gap:14px;padding-left:60px}
.topbar svg{width:12px;height:12px;fill:#fff;margin-right:5px;vertical-align:-1px}
.brand{display:flex;align-items:center;gap:8px;color:var(--blue);font-weight:700;font-size:19px}
.brand .dot{width:22px;height:22px;border-radius:50%;background:var(--magenta)}
.header-brand{left:172px;top:38px}
.nav{left:409px;top:58px;display:flex;gap:30px;font-size:14.5px;color:var(--ink)}
.nav .active{color:var(--magenta);border-bottom:2px solid var(--magenta);padding-bottom:2px}
.btn{display:inline-flex;align-items:center;gap:7px;font-weight:500;font-size:14.5px}
.btn-solid{background:var(--blue);color:#fff;padding:0 14px;height:40px;border-radius:2px}
.btn-line{border:2px solid #fff;color:#fff;padding:0 16px;height:40px;border-radius:3px}
.btn svg{width:11px;height:11px}
.cta-top{left:864px;top:50px}

/* hero */
.hero{left:0;top:105px;width:1200px;height:437px;background:linear-gradient(180deg,#8c96a2 0%,#b7bec6 45%,#5d636b 100%)}
.hero-van{position:absolute;left:150px;top:50px;width:480px;height:350px;border-radius:30px;background:linear-gradient(160deg,#e4e7ea,#a8afb6)}
.hero-text{left:659px;top:230px;color:#fff}
.hero-text .kicker{font-size:28px;font-weight:300}
.hero-text h1{font-size:44px;font-weight:700;line-height:1.25;margin-top:4px}
.hero-text .btn{margin-top:16px;height:38px}
.arrow{top:175px;width:50px;height:84px;background:rgba(40,45,55,.55);display:flex;align-items:center;justify-content:center}

/* services */
.section-title{width:1200px;left:0;text-align:center;font-size:39px;color:var(--blue);font-weight:300}
.section-title b{color:var(--ink);font-weight:700}
.card{top:693px;width:268px;height:209px;background:#fff;border-radius:0 0 60px 0;box-shadow:0 4px 18px rgba(20,40,90,.12);padding:86px 22px 0}
.card p{font-size:13.5px;line-height:1.7;color:#222}
.card .tab{position:absolute;left:0;top:0;width:92px;height:76px;background:var(--magenta);clip-path:polygon(0 0,100% 0,50% 100%,0 100%)}
.card .tab svg{position:absolute;left:18px;top:10px;width:38px;height:38px;stroke:#fff;fill:none;stroke-width:1.6}
.circle-nav{width:36px;height:36px;border-radius:50%;display:flex;align-items:center;justify-content:center}

/* about */
.about{left:0;top:1000px;width:1200px;height:505px;background:radial-gradient(circle at 10% 10%,#1450c9 0%,var(--blue) 40%,var(--blue-dark) 100%)}
.about-text{left:174px;top:1110px;color:#fff;width:400px}
.about-text .kicker{font-size:24px}
.about-text h2{font-size:35px;font-weight:700;line-height:1.2;white-space:nowrap}
.about-text p{font-size:13.5px;line-height:1.85;margin:22px 0 30px}
.about-photo{left:615px;top:1068px;width:386px;height:383px;background:linear-gradient(135deg,#c9a089,#5f8fb2 60%,#2b3440);border-radius:24px}

/* reserve */
.reserve{left:0;top:1505px;width:1200px;height:497px;background:linear-gradient(90deg,#fff 40%,#f1f3f7 100%)}
.reserve-text{left:172px;top:1625px;width:530px}
.reserve-text h2{font-size:37px;font-weight:400;color:var(--blue);line-height:1.3}
.reserve-text h2 b{display:block;color:var(--ink);font-weight:700;font-size:38px}
.reserve-text p{font-size:13.5px;line-height:1.7;margin-top:24px;color:#333}
.cal{left:742px;top:1598px;width:284px;height:242px;background:var(--magenta);border-radius:4px;color:#fff;font-size:11px;padding:8px 6px}
.cal-head{display:flex;justify-content:space-between;padding:0 12px;font-size:13px;font-weight:600;height:22px;align-items:center}
.cal-grid{display:grid;grid-template-columns:repeat(7,1fr);text-align:center}
.cal-grid span{height:31px;line-height:31px}
.cal-grid .dow{height:20px;line-height:20px;font-size:9px;font-weight:600}
.cal-grid .b{font-weight:700}
.cal-grid .mut{opacity:.75}
.cal-grid .on{background:#2d6be6;border-radius:3px;font-weight:700;margin:3px 6px;height:25px;line-height:25px}
.cal-grid .soft{background:#4a6fd6;border-radius:3px;margin:3px 6px;height:25px;line-height:25px}

/* process */
.process{left:0;top:2002px;width:1200px;height:499px;background:var(--light)}
.step{width:220px;text-align:center}
.step h3{font-size:15px;font-weight:600;letter-spacing:1px;margin-bottom:10px}
.step p{font-size:13.5px;line-height:1.7;color:#333}

/* contact */
.touch{left:0;top:2501px;width:1200px;height:400px;background:radial-gradient(circle at 15% 20%,#1552cc,var(--blue) 50%,var(--blue-dark))}
.phone{left:118px;top:2481px;width:260px;height:366px;background:linear-gradient(160deg,#17d7e6,#12e8b9);border-radius:36px}
.touch-title{left:492px;top:2581px;color:#fff;font-size:39px;font-weight:300}
.touch-title b{font-weight:700}
.field{height:39px;background:#fff;border:1px solid #c9d3ea;font-size:13.5px;color:#333;padding:0 9px;display:flex;align-items:center;justify-content:space-between;width:262px}
.submit{left:492px;top:2756px;height:38px;border:2px solid #fff;color:#fff;padding:0 12px;border-radius:2px}

/* footer */
.foot-h{font-size:18px;font-weight:700;color:var(--blue)}
.foot-list{font-size:14px;color:#333;line-height:36px;list-style:none}
.foot-sep{width:1px;background:#9aa8d0}
.foot-sep i{position:absolute;left:-2px;top:55px;width:4px;height:24px;background:var(--magenta)}
.social{display:flex;gap:8px}
.social span{width:25px;height:25px;border-radius:50%;background:var(--blue)}
.copy{font-size:11.5px;color:#333}
.copy b{color:var(--blue);font-weight:500}
</style>
</head>
<body>

<!-- header -->
<div class="topbar">
  <span><svg viewBox="0 0 24 24"><path d="M6.6 10.8a15.2 15.2 0 006.6 6.6l2.2-2.2a1 1 0 011-.25 11.4 11.4 0 003.6.57 1 1 0 011 1V20a1 1 0 01-1 1A17 17 0 013 4a1 1 0 011-1h3.5a1 1 0 011 1c0 1.25.2 2.45.57 3.57a1 1 0 01-.25 1z"/></svg>555-014-2288</span>
  <span><svg viewBox="0 0 24 24"><path d="M2 5h20v14H2z M2 5l10 8 10-8" fill="#fff" stroke="#0b2150" stroke-width="1.5"/></svg>info@vcaravan.example</span>
</div>
<div class="abs brand header-brand"><span class="dot"></span>Vitality Caravan</div>
<nav class="abs nav">
  <a class="active">Home</a><a>About</a><a>Services</a><a>Schedule Today</a><a>Pricing</a>
</nav>
<a class="abs btn btn-solid cta-top">Get Your Vaccine <svg viewBox="0 0 12 12"><circle cx="6" cy="6" r="6" fill="#fff"/><path d="M5 3l3 3-3 3" stroke="#0a3aa8" stroke-width="1.6" fill="none"/></svg></a>

<!-- hero -->
<section class="abs hero">
  <div class="hero-van" role="img" aria-label="White branded vaccination van driving through a city street"></div>
  <div class="abs arrow" style="left:0"><svg width="30" height="50" viewBox="0 0 30 50"><path d="M24 4L6 25l18 21" stroke="#fff" stroke-width="2" fill="none"/></svg></div>
  <div class="abs arrow" style="right:0"><svg width="30" height="50" viewBox="0 0 30 50"><path d="M6 4l18 21-18 21" stroke="#fff" stroke-width="2" fill="none"/></svg></div>
</section>
<div class="abs hero-text">
  <div class="kicker">Making the workplace</div>
  <h1>A Healthier Place</h1>
  <a class="btn btn-solid">Contact Us <svg viewBox="0 0 12 12"><circle cx="6" cy="6" r="6" fill="#fff"/><path d="M5 3l3 3-3 3" stroke="#0a3aa8" stroke-width="1.6" fill="none"/></svg></a>
</div>

<!-- services -->
<h2 class="abs section-title" style="top:600px">Vaccination <b>Services</b></h2>
<div class="abs circle-nav" style="left:151px;top:784px;background:#d9dce3"><svg width="12" height="14" viewBox="0 0 12 14"><path d="M9 2L3 7l6 5" stroke="#fff" stroke-width="2" fill="none"/></svg></div>
<div class="abs card" style="left:172px">
  <div class="tab"><svg viewBox="0 0 40 40"><rect x="6" y="16" width="14" height="18" rx="2"/><path d="M9 12h8v4M13 22v8M9 26h8M28 6l4 4M30 8l-4 20-4-2 4-20"/></svg></div>
  <p>Vitality Caravan specializes in providing seamless, hassle-free, on-site mobile vaccine clinics.</p>
</div>
<div class="abs card" style="left:466px">
  <div class="tab"><svg viewBox="0 0 40 40"><circle cx="20" cy="10" r="5"/><path d="M20 8v2h2M4 26h32M6 26v6M34 26v6"/><rect x="7" y="20" width="7" height="6"/><rect x="17" y="20" width="7" height="6"/><rect x="27" y="20" width="7" height="6"/></svg></div>
  <p>No crowded waiting rooms, no long lines, no hassle!</p>
</div>
<div class="abs card" style="left:759px;padding-top:78px">
  <div class="tab"><svg viewBox="0 0 40 40"><rect x="4" y="12" width="32" height="22" rx="2"/><rect x="14" y="4" width="12" height="8"/><path d="M20 6v5M17.5 8.5h5M8 20h24v10H8zM20 20v10"/></svg></div>
  <p>Specializing in workplace mployee vaccine clinics. Great service to offer as part of your company’s Employee Wellness Package.</p>
</div>
<div class="abs circle-nav" style="left:1011px;top:784px;background:var(--blue)"><svg width="12" height="14" viewBox="0 0 12 14"><path d="M3 2l6 5-6 5" stroke="#fff" stroke-width="2" fill="none"/></svg></div>

<!-- about -->
<section class="abs about"></section>
<div class="abs about-photo" role="img" aria-label="Woman in a face mask receiving a vaccine injection in her arm"></div>
<div class="abs about-text">
  <div class="kicker">About</div>
  <h2>Vitality Caravan, PLLC</h2>
  <p>Vitality Caravan, PLLC mission: Making the workplace a healthier place.To provide on-site wellness services to employers that simplify and streamline employee preventative health.</p>
  <a class="btn btn-line">Read More <svg viewBox="0 0 12 12"><circle cx="6" cy="6" r="6" fill="#fff"/><path d="M5 3l3 3-3 3" stroke="#0a3aa8" stroke-width="1.6" fill="none"/></svg></a>
</div>

<!-- reserve -->
<section class="abs reserve"></section>
<div class="abs reserve-text">
  <h2>Reserve your on-site mobile <b>Vaccine clinic today!</b></h2>
  <p>Lorem ipsum dolor sit amet, consectetur adipiscing elit. Sed ligula nulla, finibus non tempor at, posuere id massa. Donec eu dapibus nisl. Etiam a nunc lorem. Vivamus id tristique lacus.</p>
</div>
<div class="abs cal">
  <div class="cal-head"><span>◂</span><span>February <span style="font-weight:400">2022</span></span><span>▸</span></div>
  <div class="cal-grid">
    <span class="dow">Sun</span><span class="dow">Mon</span><span class="dow">Tue</span><span class="dow">Wed</span><span class="dow">Thu</span><span class="dow">Fri</span><span class="dow">Sat</span>
    <span class="mut">28</span><span class="mut">29</span><span>1</span><span>2</span><span>3</span><span class="b">4</span><span class="b">5</span>
    <span class="b">6</span><span class="b">7</span><span class="soft">8</span><span class="b">9</span><span class="b">10</span><span class="b">11</span><span>12</span>
    <span>13</span><span>14</span><span>15</span><span>16</span><span>17</span><span>18</span><span>19</span>
    <span>20</span><span>21</span><span>22</span><span>23</span><span>24</span><span>25</span><span>26</span>
    <span>27</span><span>28</span><span class="on">29</span><span>30</span><span>31</span><span class="mut">1</span><span class="mut">2</span>
    <span class="mut">3</span><span class="mut">4</span><span class="mut">5</span><span class="mut">6</span><span class="mut">7</span><span class="mut">8</span><span class="mut">9</span>
  </div>
</div>

<!-- process -->
<section class="abs process">
  <svg class="abs" style="left:0;top:0" width="1200" height="499" viewBox="0 0 1200 499">
    <defs>
      <linearGradient id="flow" x1="0" x2="1"><stop offset="0" stop-color="#4a5fb3"/><stop offset=".5" stop-color="#3aabb8"/><stop offset="1" stop-color="#a04a9c"/></linearGradient>
    </defs>
    <path d="M395 168 A134 134 0 1 0 455 330 C480 260 510 135 601 135 C660 135 700 175 718 208" fill="none" stroke="url(#flow)" stroke-width="5"/>
    <path d="M481 336 C520 390 560 404 601 404 C700 404 740 330 765 250 C790 175 830 135 893 135 A134 134 0 1 1 805 370" fill="none" stroke="url(#flow)" stroke-width="5"/>
    <circle cx="395" cy="168" r="9" fill="#4f75b8"/><circle cx="718" cy="208" r="9" fill="#3aabb8"/>
    <circle cx="481" cy="336" r="9" fill="#3aabb8"/><circle cx="805" cy="370" r="9" fill="#8d5aa2"/>
  </svg>
</section>
<h2 class="abs section-title" style="top:2055px">Our <b>Process</b></h2>
<div class="abs step" style="left:199px;top:2232px"><h3 style="color:#4a64ae">STEP 1</h3><p>Submit Vaccine Clinic Needs Questionnaire.</p></div>
<div class="abs step" style="left:491px;top:2232px"><h3 style="color:var(--teal)">STEP 2</h3><p>Vitality Caravan, PLLC will contact you to schedule on-site vaccine clinic.</p></div>
<div class="abs step" style="left:783px;top:2232px"><h3 style="color:var(--magenta)">STEP 3</h3><p>Prepare your employees for vaccine clinic day.</p></div>

<!-- contact -->
<section class="abs touch"></section>
<div class="abs phone" role="img" aria-label="Hand holding a smartphone showing the booking screen with an OTP entry"></div>
<h2 class="abs touch-title">Get <b>In Touch</b></h2>
<div class="abs field" style="left:493px;top:2650px">Business Name</div>
<div class="abs field" style="left:763px;top:2650px">Location</div>
<div class="abs field" style="left:493px;top:2699px">Contct Person Info</div>
<div class="abs field" style="left:763px;top:2699px">Choose your time <svg width="12" height="8" viewBox="0 0 12 8"><path d="M1 1l5 5 5-5" stroke="#333" stroke-width="1.6" fill="none"/></svg></div>
<a class="abs btn submit">Submit Now <svg viewBox="0 0 12 12"><circle cx="6" cy="6" r="6" fill="#fff"/><path d="M5 3l3 3-3 3" stroke="#0a3aa8" stroke-width="1.6" fill="none"/></svg></a>

<!-- footer -->
<div class="abs brand" style="left:168px;top:3062px;font-size:21px"><span class="dot"></span>Vitality Caravan</div>
<div class="abs social" style="left:172px;top:3133px"><span></span><span></span><span></span></div>
<p class="abs copy" style="left:172px;top:3198px">© 2022 <b>VITALITY CARAVAN, PLLC</b>. All right reserved</p>

<div class="abs" style="left:390px;top:2996px;width:215px">
  <h3 class="foot-h">Contact Info</h3>
  <ul class="foot-list" style="margin-top:10px">
    <li><svg width="14" height="14" viewBox="0 0 24 24" style="vertical-align:-2px;margin-right:10px"><path fill="#9b2a8f" d="M6.6 10.8a15.2 15.2 0 006.6 6.6l2.2-2.2a1 1 0 011-.25 11.4 11.4 0 003.6.57 1 1 0 011 1V20a1 1 0 01-1 1A17 17 0 013 4a1 1 0 011-1h3.5a1 1 0 011 1c0 1.25.2 2.45.57 3.57a1 1 0 01-.25 1z"/></svg>555-014-2288</li>
    <li><svg width="14" height="12" viewBox="0 0 24 20" style="vertical-align:-1px;margin-right:10px"><rect width="24" height="20" fill="#9b2a8f"/><path d="M0 0l12 10L24 0" stroke="#fff" stroke-width="2" fill="none"/></svg>info@vcaravan.example</li>
  </ul>
</div>
<div class="abs foot-sep" style="left:616px;top:2995px;height:213px"><i></i></div>
<div class="abs" style="left:679px;top:2996px">
  <h3 class="foot-h">Useful Links</h3>
  <ul class="foot-list" style="margin-top:10px"><li>Home</li><li>About</li><li>Services</li><li>Schedule Today</li><li>Pricing</li></ul>
</div>
<div class="abs foot-sep" style="left:867px;top:2995px;height:213px"><i></i></div>
<div class="abs" style="left:905px;top:2996px">
  <h3 class="foot-h">Other Links</h3>
  <ul class="foot-list" style="margin-top:10px"><li>Privacy Policy</li><li>Contact Us</li><li>Terms &amp; Condition</li><li>Cookies</li></ul>
</div>

</body>
</html>
```